Update patient consent forms and contract

Objective
Redesign the existing patient contract information document to create a modern,contempory, and easy-to-understand experience for patients. The updated design should improve readability, accessibility, and overall presentation while maintaining compliance with healthcare and legal requirements.

Key Deliverables

Refreshed visual design and layout
Improved information hierarchy and readability
Modern typography and colour palette aligned with brand guidelines
Clear section headings and navigation
Print-ready and digital versions (PDF)

Include KEV Logo within patient KEV consent to treatment. Ideally this document should be portrait not landscape.
Updates

I would love a front page to be included in the document

```html
<!DOCTYPE html>
<html lang="en">
<head>
<meta charset="utf-8">
<title>KEV Orthodontic Treatment Consent</title>
<link rel="stylesheet" href="https://fonts.googleapis.com/css2?family=Outfit:wght@500;600;700&family=Poppins:wght@300;400&display=swap">
<style>
  :root{
    --stage:#3f434d;
    --navy:#0b1a4a;
    --navy-deep:#031a4b;
    --stone:#767871;
    --strip:#2f4677;
    --paper:#ffffff;
    --rule:#cfd0d3;
    --ink:#2a2d36;
    --muted:#6f706b;
  }
  *{margin:0;padding:0;box-sizing:border-box}
  html,body{width:1200px;height:1000px;overflow:hidden;background:var(--stage)}
  .canvas{position:relative;width:1200px;height:1000px;background:var(--stage)}
  .page{position:absolute;top:134px;width:517px;height:732px;background:var(--paper);overflow:hidden}
  .cover{left:72px}
  .inner{left:612px}

  .cover-shapes{position:absolute;inset:0;width:100%;height:100%}
  .brand{position:absolute;left:74px;top:104px;display:flex;align-items:center;gap:10px}
  .brand-dot{width:22px;height:22px;border-radius:50%;background:var(--stone)}
  .brand-name{font-family:"Poppins",sans-serif;font-weight:300;font-size:16px;line-height:1.05;color:var(--stone)}
  .cover-title{position:absolute;left:64px;top:244px;font-family:"Outfit",sans-serif;font-weight:700;font-size:42px;line-height:43px;color:var(--navy);letter-spacing:.2px}
  .cover-rule{position:absolute;left:64px;top:386px;width:65px;height:3px;background:var(--stone)}
  .cover-sub{position:absolute;left:64px;top:414px;font-family:"Poppins",sans-serif;font-weight:300;font-size:18px;line-height:26px;color:var(--muted)}

  .running-head{position:absolute;left:46px;top:46px;font-family:"Poppins",sans-serif;font-size:10px;color:var(--navy);letter-spacing:.1px}
  .running-rule{position:absolute;left:46px;top:67px;width:443px;height:1px;background:var(--rule)}
  .section-title{position:absolute;font-family:"Outfit",sans-serif;font-weight:600;color:var(--navy);font-size:21px;line-height:24px}
  .section-rule{position:absolute;background:var(--rule)}
  .body-copy{position:absolute;font-family:"Poppins",sans-serif;font-size:6.6px;line-height:11px;color:var(--ink)}

  .treatment-title{left:42px;top:101px}
  .treatment-rule{left:42px;top:157px;width:212px;height:1px}
  .treatment-copy{left:42px;top:168px;width:214px}
  .photo-strip{position:absolute;left:269px;top:97px;width:19px;height:297px;background:var(--strip)}
  .photo-patient{position:absolute;left:288px;top:97px;width:229px;height:297px;background:linear-gradient(150deg,#9fb3be 0%,#c9cfcf 40%,#e9dccf 60%,#b7c6d6 100%)}
  .photo-smile{position:absolute;left:0;top:394px;width:269px;height:289px;background:linear-gradient(120deg,#eadfd6 0%,#c9d9e8 45%,#8fb4d6 75%,#dfe9f1 100%)}
  .benefits-title{left:291px;top:437px}
  .benefits-rule{left:291px;top:467px;width:183px;height:4px}
  .benefits-copy{left:291px;top:480px;width:203px}
</style>
</head>
<body>
<div class="canvas">

  <section class="page cover">
    <svg class="cover-shapes" viewBox="0 0 645 914" preserveAspectRatio="none" aria-hidden="true">
      <rect width="645" height="914" fill="var(--navy-deep)"/>
      <circle cx="170" cy="330" r="555" fill="var(--paper)"/>
      <circle cx="150" cy="340" r="549" fill="var(--stone)"/>
      <ellipse cx="170" cy="380" rx="430" ry="450" fill="var(--paper)"/>
    </svg>
    <div class="brand">
      <span class="brand-dot"></span>
      <span class="brand-name">KEV<br>Orthodontists</span>
    </div>
    <h1 class="cover-title">Orthodontic<br>Treatment<br>Consent</h1>
    <div class="cover-rule"></div>
    <p class="cover-sub">Patient Information &amp;<br>Treatment Agreement</p>
  </section>

  <section class="page inner">
    <p class="running-head">KEV ORTHODONTISTS</p>
    <div class="running-rule"></div>

    <h2 class="section-title treatment-title">Orthodontic<br>Treatment</h2>
    <div class="section-rule treatment-rule"></div>
    <p class="body-copy treatment-copy">Orthodontic treatment promotes a healthy smile, healthier teeth and gums and a better bite for normal chewing. Orthodontic treatment depends for much of its success on the understanding and co-operation of the patient. This form covers the usual material risks associated with Orthodontic treatment. You may ask your orthodontist to explain anything you do not understand. While recognizing he benefits of healthy teeth and a pleasing smile, you should also be aware that orthodontic treatment has limitations and potential risks and there may be alternative treatment options. You should clarify what is expected of you as a patient, or as the parent of a young patient, to achieve excellent results. Keep in mind that with orthodontic treatment, like other healing arts, results cannot be guaranteed. The unknown factor in any orthodontic correction is the response of the patient to the orthodontic treatment. Should you have any questions please ask.</p>

    <div class="photo-strip"></div>
    <div class="photo-patient" role="img" aria-label="Photo of a smiling patient reclined in a dental chair while a gloved clinician works"></div>
    <div class="photo-smile" role="img" aria-label="Photo of a smiling young woman in a dental chair with a masked orthodontist beside her"></div>

    <h2 class="section-title benefits-title">Benefits</h2>
    <div class="section-rule benefits-rule"></div>
    <p class="body-copy benefits-copy">Orthodontics plays an important role in improving overall oral health and achieving balance and harmony between the face and teeth for a beautiful, healthy smile, which may enhance one's self esteem. The correct bite of teeth with health muscles and jaw joints will provide optimal chewing function. Properly aligned teeth are easier to brush and so the tendancy to decay may be decreased, as may the likelihood of developing disease of the gums and supporting bone Correctly aligned teeth are less likely to experience abnormal wear. Because of the individual conditions present and the limitations of treatment imposed by the nature each specific benefit may not be attainable for every patient.</p>
  </section>

</div>
</body>
</html>
```